Quillmere Voyage Care Web Page

To create a web page that has the number 1 goal of converting Zorvix Ad / Trellisgram Ads clicks into paying customers.
The site will feed into a web application where travellers can enter their trip and purchase a Voyawell Ready Pack.
The page / site needs to be able to tell people what we do and encourage them to start the process of getting a Voyawell Ready Pack.
It should be a wordpress theme.
Please see the attached brief for more information.

```html
<!DOCTYPE html>
<html lang="en">
<head>
<meta charset="utf-8">
<title>Quillmere Voyage Care</title>
<link href="https://fonts.googleapis.com/css2?family=Lexend:wght@400;500;600&family=Arimo:wght@400;700&display=swap" rel="stylesheet">
<style>
:root{
  --navy:#1b2448;
  --footer:#1f2a56;
  --blue:#4ba3cf;
  --cyan:#36acd0;
  --band-a:#52a6d1;
  --band-b:#3e6f96;
  --grey-bg:#f1f1f1;
  --text:#6b7280;
  --white:#ffffff;
}
*{margin:0;padding:0;box-sizing:border-box}
html,body{width:1200px;height:4570px;overflow:hidden;background:var(--white)}
body{position:relative;font-family:"Arimo",Arial,sans-serif;color:var(--text)}
.abs{position:absolute}
h1,h2,h3,.nav a,.btn,.phone,.cta-text{font-family:"Lexend",Arial,sans-serif}
.btn{position:absolute;display:flex;align-items:center;justify-content:center;border-radius:999px;font-size:18px;font-weight:500;color:var(--white);text-decoration:none}
.btn-fill{background:linear-gradient(90deg,#4d9fcb,#3a6f98)}
.btn-line{border:2px solid var(--white)}
.photo{position:absolute;border-radius:18px}
h2{font-size:40px;line-height:48px;font-weight:500;color:var(--navy)}
h2 .accent{color:var(--blue)}
.copy{font-size:14.5px;line-height:18.3px;color:var(--text)}

.header{position:absolute;left:0;top:0;width:1200px;height:138px;background:var(--white)}
.brand-disc{position:absolute;left:102px;top:10px;width:170px;height:170px;border-radius:50%;background:var(--white)}
.brand{position:absolute;left:102px;top:92px;width:170px;text-align:center;font-family:"Lexend",sans-serif;font-weight:500;color:var(--navy)}
.brand .name{font-size:26px;line-height:30px}
.brand .tag{font-size:11.5px;letter-spacing:.5px}
.phone{position:absolute;left:675px;top:36px;font-size:19px;color:var(--blue);display:flex;align-items:center;gap:8px}
.nav a{position:absolute;top:90px;font-size:17px;font-weight:500;color:var(--navy);text-decoration:none}

.hero{position:absolute;left:0;top:138px;width:1200px;height:568px;
  background:linear-gradient(180deg,#b9d3dc 0%,#6d9fb4 40%,#1f6786 70%,#2e4a3c 100%)}
.hero h1{position:absolute;left:124px;top:156px;font-size:66px;line-height:68px;font-weight:500;color:var(--white)}

.brief{position:absolute;left:0;top:706px;width:1200px;height:537px;background:var(--grey-bg)}

.band-blue{position:absolute;left:0;top:1777px;width:1200px;height:580px;background:linear-gradient(90deg,var(--band-a),var(--band-b))}
.band-cyan{position:absolute;left:0;top:2893px;width:1200px;height:623px;background:var(--cyan)}
.frame{position:absolute;border:2.5px solid var(--white);border-radius:20px}
.band-title{color:var(--white)}
.bullets{list-style:none;color:var(--white);font-size:14.5px;line-height:29px}
.bullets li::before{content:"";display:inline-block;width:9px;height:9px;border-radius:50%;background:var(--white);margin-right:12px;vertical-align:1px}

.cta{position:absolute;left:0;top:4054px;width:1200px;height:130px;background:var(--cyan)}
.cta-text{position:absolute;left:126px;top:52px;font-size:24px;font-weight:500;color:var(--white)}

.footer{position:absolute;left:0;top:4184px;width:1200px;height:386px;background:var(--footer)}
.vline{position:absolute;top:0;width:1px;height:289px;background:#34406b}
.hline{position:absolute;left:0;top:307px;width:1200px;height:1px;background:#34406b}
.f-head{position:absolute;font-family:"Lexend",sans-serif;font-size:22px;font-weight:500;color:var(--blue)}
.f-list{position:absolute;list-style:none;font-size:14.5px;line-height:25.7px;color:var(--white)}
.f-brand{position:absolute;left:126px;top:180px;font-family:"Lexend",sans-serif;font-weight:500;color:var(--white)}
.f-brand .name{font-size:34px;line-height:38px}
.f-brand .tag{font-size:16px;letter-spacing:.5px}
.f-brand-disc{position:absolute;left:140px;top:80px;width:80px;height:80px;border-radius:50%;background:var(--blue)}
.contact{position:absolute;left:834px;display:flex;align-items:center;gap:16px;color:var(--white);font-size:14.5px;line-height:21px}
.c-icon{width:50px;height:50px;border-radius:50%;background:var(--blue);display:flex;align-items:center;justify-content:center;flex:none}
.social{position:absolute;width:36px;height:36px;border-radius:50%;border:2px solid var(--white);background:transparent}
.copyright{position:absolute;right:128px;top:333px;font-size:14px;color:var(--white)}
</style>
</head>
<body>

<header class="header">
  <div class="brand-disc"></div>
  <div class="brand"><div class="name">quillmere</div><div class="tag">VOYAGE CARE</div></div>
  <div class="phone">
    <svg width="16" height="16" viewBox="0 0 24 24" fill="#4ba3cf"><path d="M6.6 10.8a15 15 0 0 0 6.6 6.6l2.2-2.2c.3-.3.7-.4 1-.2 1.1.4 2.3.6 3.6.6.6 0 1 .4 1 1V20c0 .6-.4 1-1 1A17 17 0 0 1 3 4c0-.6.4-1 1-1h3.5c.6 0 1 .4 1 1 0 1.3.2 2.5.6 3.6.1.3 0 .7-.2 1z"/></svg>
    Call Us: 555 010 4821
  </div>
  <a class="btn btn-fill" href="#" style="left:937px;top:25px;width:135px;height:46px">Buy Now</a>
  <nav class="nav">
    <a href="#" style="left:414px">Home</a>
    <a href="#" style="left:515px">About Us</a>
    <a href="#" style="left:643px">What is a Travel Health</a>
    <a href="#" style="left:889px">Disease</a>
    <a href="#" style="left:1005px">Country</a>
  </nav>
</header>

<section class="hero" role="img" aria-label="Travellers celebrating on a mountain summit above a coastal fjord">
  <h1>Quillmere<br>Voyage Care</h1>
  <a class="btn btn-line" href="#" style="left:128px;top:316px;width:138px;height:52px">Buy Now</a>
</section>

<section class="brief">
  <div class="photo" role="img" aria-label="Traveller in a straw hat on a rope bridge through a forest" style="left:128px;top:105px;width:467px;height:339px;background:linear-gradient(160deg,#4f6b3a,#9a8a6a 55%,#3b4a2c)"></div>
  <h2 class="abs" style="left:639px;top:122px">Voyawell <span class="accent">Ready Pack</span></h2>
  <p class="copy abs" style="left:639px;top:206px;width:418px">Lorem ipsum dolor sit amet, consectetur adipiscing elit, sedo eiusmod tempor incididunt ut labore et dolore magna aliqua. Quis ipsum suspendisse ultrices gravida. Risus commodo viverra maecenas accumsan lacus vel facilisis. r incididunt ut labore et dolore magna aliqua. Quis ipsum suspendisse ultrices gravida. Risus commodo viverra maecenas accums an lacus vel facilisis.</p>
  <a class="btn btn-fill" href="#" style="left:639px;top:363px;width:151px;height:49px">Buy Now</a>
</section>

<section>
  <h2 class="abs" style="left:126px;top:1354px">What is <span class="accent">quillmere</span><br><span class="accent">voyage care?</span></h2>
  <p class="copy abs" style="left:126px;top:1470px;width:415px">Lorem ipsum dolor sit amet, consectetur adipiscing elit, sedo eiusmod tempor incididunt ut labore et dolore magna aliqua. Quis ipsum suspendisse ultrices gravida. Risus commodo viverra maecenas accumsan lacus vel facilisis. r incididunt ut labore et dolore magna aliqua. Quis ipsum suspendisse ultrices gravida. Risus commodo viverra maecenas accums an lacus vel facilisis.</p>
  <a class="btn btn-fill" href="#" style="left:128px;top:1628px;width:151px;height:48px">Read More</a>
  <div class="photo" role="img" aria-label="Two hikers with backpacks looking over a turquoise mountain lake" style="left:607px;top:1344px;width:467px;height:339px;background:linear-gradient(180deg,#9fb9c4 0%,#5e8a8f 30%,#39a3b3 60%,#2c8a9e 100%)"></div>
</section>

<section class="band-blue">
  <div class="frame" style="left:422px;top:97px;width:650px;height:396px"></div>
  <div class="photo" role="img" aria-label="Toy airplane, passports and a stethoscope on a table" style="left:133px;top:126px;width:465px;height:339px;background:linear-gradient(135deg,#d8d2cb,#9a9793 55%,#5b5e62)"></div>
  <h2 class="band-title abs" style="left:648px;top:140px;font-size:38px">Why buy a Voyawell<br>Ready Pack</h2>
  <ul class="bullets abs" style="left:650px;top:238px">
    <li>Sed et mauris vel nulla pulvinar mattis.</li>
    <li>Nullam molestie sapien vel dolor congue rutrum.</li>
    <li>Ut pulvinar sapien a enim egestas, seallis quam tristique.</li>
    <li>Curabitur facilisis nibh ut finibus porta.</li>
  </ul>
  <a class="btn btn-line" href="#" style="left:650px;top:373px;width:152px;height:49px">Buy Now</a>
</section>

<section>
  <h2 class="abs" style="left:126px;top:2463px">What is in a<br><span class="accent">Voyawell Ready Pack</span></h2>
  <p class="copy abs" style="left:126px;top:2577px;width:415px">Lorem ipsum dolor sit amet, consectetur adipiscing elit, sedo eiusmod tempor incididunt ut labore et dolore magna aliqua. Quis ipsum suspendisse ultrices gravida. Risus commodo viverra maecenas accumsan lacus vel facilisis. r incididunt ut labore et dolore magna aliqua. Quis ipsum suspendisse ultrices gravida. Risus commodo viverra maecenas accums an lacus vel facilisis.</p>
  <a class="btn btn-fill" href="#" style="left:128px;top:2734px;width:151px;height:48px">Read More</a>
  <div class="photo" role="img" aria-label="Stethoscope with a heartbeat line on a medical chart" style="left:607px;top:2457px;width:467px;height:339px;background:linear-gradient(135deg,#cfe4ee,#8fb9cf 50%,#5d8fae)"></div>
</section>

<section class="band-cyan">
  <div class="frame" style="left:422px;top:126px;width:650px;height:394px"></div>
  <div class="photo" role="img" aria-label="Traveller in a hat working on a laptop on a mountain deck" style="left:133px;top:155px;width:465px;height:339px;background:linear-gradient(135deg,#8ea4a6,#5d7467 55%,#3a4c44)"></div>
  <h2 class="band-title abs" style="left:644px;top:183px">What vaccines do<br>I need for....</h2>
  <p class="abs" style="left:646px;top:298px;width:385px;font-size:14.5px;line-height:18.3px;color:var(--white)">Lorem ipsum dolor sit amet, consectetur adipisci elit, sedo eiusmod tempor incididunt ut labore et magna aliqua. Quis ipsum suspendisse ultrices gravida.orem ipsum dolor sit amet, consectetur adipiscing elit, sedo eiusmod tempor incididunt ut labore et dolore magna aliquais ipsum suspendisse ultrices gida.</p>
  <a class="btn btn-line" href="#" style="left:648px;top:437px;width:147px;height:46px">Buy Now</a>
</section>

<section>
  <h2 class="abs" style="left:130px;top:3604px">What antimalarials<br><span class="accent">do I need for...</span></h2>
  <p class="copy abs" style="left:130px;top:3713px;width:385px;line-height:20px">Lorem ipsum dolor sit amet, consectetur adipiscing elit, sedo eiusmod tempor incididunt ut labore et dolore mag na aliqua. Quis ipsum suspendisse ultrices gravidaorem ipsum dolor sit amet, consectetur adipiscing elit, sedo eiusmod tempor incididunt ut labore et dolore magna aliqua. Quis ipsum suspendisse ultrices gravida.</p>
  <a class="btn btn-fill" href="#" style="left:130px;top:3861px;width:149px;height:48px">Buy Now</a>
  <div class="photo" role="img" aria-label="Vaccine vials and a syringe on a laboratory bench" style="left:607px;top:3614px;width:465px;height:339px;background:linear-gradient(135deg,#b8c4c2,#7f948f 50%,#c9cfc6)"></div>
</section>

<section class="cta">
  <p class="cta-text">Lorem ipsum dolor sit amet, consectetur adipiscing elit,</p>
  <a class="btn btn-line" href="#" style="left:898px;top:50px;width:146px;height:46px">Buy Now</a>
</section>

<footer class="footer">
  <div class="vline" style="left:318px"></div>
  <div class="vline" style="left:525px"></div>
  <div class="vline" style="left:751px"></div>
  <div class="hline"></div>

  <div class="f-brand-disc"></div>
  <div class="f-brand"><div class="name">quillmere</div><div class="tag">VOYAGE CARE</div></div>

  <div class="f-head" style="left:371px;top:70px">Nav</div>
  <ul class="f-list" style="left:371px;top:122px">
    <li>Home</li><li>What is Health</li><li>Contact Us</li><li>About Us</li><li>Disease</li><li>Country</li>
  </ul>

  <div class="f-head" style="left:602px;top:70px">Links</div>
  <ul class="f-list" style="left:602px;top:122px">
    <li>Disclaimer</li><li>Privacy</li><li>Terms</li><li>Refund</li>
  </ul>

  <div class="f-head" style="left:838px;top:66px">Contact Us</div>
  <div class="contact" style="top:110px">
    <span class="c-icon"><svg width="18" height="22" viewBox="0 0 24 28" fill="#fff"><path d="M12 0a10 10 0 0 0-10 10c0 7.5 10 18 10 18s10-10.5 10-18A10 10 0 0 0 12 0zm0 14a4 4 0 1 1 0-8 4 4 0 0 1 0 8z"/></svg></span>
    <span>Location Name<br>Harbor Lane 2817 (4590)</span>
  </div>
  <div class="contact" style="top:168px">
    <span class="c-icon"><svg width="20" height="20" viewBox="0 0 24 24" fill="#fff"><path d="M6.6 10.8a15 15 0 0 0 6.6 6.6l2.2-2.2c.3-.3.7-.4 1-.2 1.1.4 2.3.6 3.6.6.6 0 1 .4 1 1V20c0 .6-.4 1-1 1A17 17 0 0 1 3 4c0-.6.4-1 1-1h3.5c.6 0 1 .4 1 1 0 1.3.2 2.5.6 3.6.1.3 0 .7-.2 1z"/></svg></span>
    <span>Phone:555.014.2290</span>
  </div>
  <div class="contact" style="top:230px">
    <span class="c-icon"><svg width="20" height="16" viewBox="0 0 24 18" fill="#fff"><path d="M0 2l12 7 12-7V0H0zm0 3v13h24V5l-12 7z"/></svg></span>
    <span>hello@quillmere.example</span>
  </div>

  <span class="social" style="left:124px;top:324px"></span>
  <span class="social" style="left:170px;top:324px"></span>
  <span class="social" style="left:216px;top:324px"></span>
  <span class="social" style="left:262px;top:324px"></span>
  <p class="copyright">© 2023 All Rights Reserved.Terms &amp; Conditions Privacy Policy</p>
</footer>

</body>
</html>
```